Business Card Design Project

We are VT Meridian, a recruitment company based in London. We require a new business card design in order to present our business. We work in a number of areas recruiting professional in areas such as engineering and rail. Most of our work is based in the Middle East so our cards must have a universal, professional feel.

Visit our website: http://www.vt-meridian.example.co.uk/ for more info

Industry/Entity Type

Business

Requirements
Must have
• Must be double sided

Must feature the companies logo on both sides of the card

Should incorporate the primary colours of the logo

Must be professional and contemporary, to fit in with the logo

Info: Name: Colin Prewett certRP MREC
Senior Recruitment Consultant
Address: 7 Quarry Row Fulwell London N41QZ
T: +44 (0)203 555 0147
M: +44 (0)7700 900 318
E: cprewett@vt-meridian.example.co.uk
W www.vt-meridian.example.co.uk
Nice to have
• A modern style card

```html
<!DOCTYPE html>
<html lang="en">
<head>
<meta charset="utf-8">
<title>VT Meridian — Business Card</title>
<link rel="stylesheet" href="https://fonts.googleapis.com/css2?family=Open+Sans:wght@400;700&family=Questrial&display=swap">
<style>
  :root {
    --stage: #e4e4e4;
    --front-light: #8c8c8c;
    --front-dark: #6a6a6a;
    --paper: #f6f6f4;
    --brand-green: #1a9e7a;
    --ink: #5a5a5a;
    --ink-soft: #777777;
    --rule: #8a8a8a;
    --white: #ffffff;
  }
  * { box-sizing: border-box; margin: 0; padding: 0; }
  html, body { width: 1200px; height: 900px; overflow: hidden; }
  body {
    background: var(--stage);
    font-family: "Questrial", "Century Gothic", sans-serif;
    position: relative;
  }
  .card {
    position: absolute;
    left: 300px;
    width: 600px;
    height: 360px;
    box-shadow: 0 10px 28px rgba(0,0,0,0.18);
  }
  .card--front {
    top: 60px;
    background: linear-gradient(135deg, var(--front-light), var(--front-dark));
    display: flex;
    align-items: center;
    justify-content: center;
  }
  .card--back {
    top: 470px;
    background: var(--paper);
  }

  /* brand lockup */
  .brand { display: flex; align-items: center; gap: 10px; }
  .brand__dot { width: 34px; height: 34px; border-radius: 50%; }
  .brand__name {
    font-family: "Questrial", "Century Gothic", sans-serif;
    font-size: 44px;
    letter-spacing: -0.5px;
    line-height: 1;
  }
  .card--front .brand__dot { background: var(--white); }
  .card--front .brand__name { color: var(--white); }
  .card--back .brand { position: absolute; left: 40px; top: 128px; }
  .card--back .brand__dot { background: var(--brand-green); }
  .card--back .brand__name { color: var(--ink); font-size: 40px; }

  /* person block */
  .person {
    position: absolute;
    right: 50px;
    top: 56px;
    text-align: right;
  }
  .person__name {
    font-family: "Open Sans", Arial, sans-serif;
    font-weight: 700;
    font-size: 15px;
    color: var(--brand-green);
  }
  .person__role {
    font-size: 13px;
    color: var(--ink-soft);
    margin-top: 1px;
  }
  .rule { position: absolute; height: 1px; background: var(--rule); }
  .rule--top { left: 300px; right: 50px; top: 104px; }
  .rule--bottom { left: 40px; width: 300px; top: 236px; }

  .address {
    position: absolute;
    right: 50px;
    top: 126px;
    text-align: right;
    font-size: 13px;
    line-height: 1.45;
    color: var(--ink-soft);
  }
  .icon { width: 16px; height: 16px; flex: none; }
  .icon--home { position: absolute; right: 26px; top: 108px; }

  .contacts {
    position: absolute;
    left: 40px;
    top: 248px;
    list-style: none;
  }
  .contacts__item {
    display: flex;
    align-items: center;
    gap: 10px;
    font-size: 14px;
    color: var(--ink);
    height: 22px;
  }
</style>
</head>
<body>

<section class="card card--front" aria-label="Card front">
  <div class="brand">
    <span class="brand__dot"></span>
    <span class="brand__name">VT Meridian</span>
  </div>
</section>

<section class="card card--back" aria-label="Card back">
  <div class="brand">
    <span class="brand__dot"></span>
    <span class="brand__name">VT Meridian</span>
  </div>

  <div class="person">
    <p class="person__name">Colin Prewett certRP MREC</p>
    <p class="person__role">Senior Recruitment Consultant</p>
  </div>
  <div class="rule rule--top"></div>
  <svg class="icon icon--home" viewBox="0 0 16 16" aria-hidden="true">
    <circle cx="8" cy="8" r="8" fill="var(--brand-green)"/>
    <path d="M4 8.2 8 4.6l4 3.6M5.3 7.4V11.4h5.4V7.4" fill="none" stroke="#fff" stroke-width="1.3"/>
  </svg>
  <address class="address" style="font-style:normal">
    7 Quarry Row London<br>N41QZ
  </address>

  <div class="rule rule--bottom"></div>
  <ul class="contacts">
    <li class="contacts__item">
      <svg class="icon" viewBox="0 0 16 16" aria-hidden="true"><circle cx="8" cy="8" r="8" fill="var(--brand-green)"/><path d="M5.2 4.4c.6-.4 1.1-.3 1.4.3l.6 1.2c.2.5 0 .8-.4 1.1.4.9 1.2 1.8 2.1 2.2.3-.4.6-.6 1.1-.4l1.2.6c.6.3.7.8.3 1.4-.7 1-2 1.1-3.4.2C6.8 9.9 5.9 9 5.2 7.8c-.8-1.4-.8-2.7 0-3.4z" fill="#fff"/></svg>
      +44 (0)203 555 0147
    </li>
    <li class="contacts__item">
      <svg class="icon" viewBox="0 0 16 16" aria-hidden="true"><circle cx="8" cy="8" r="8" fill="var(--brand-green)"/><rect x="5.6" y="3.6" width="4.8" height="8.8" rx="0.9" fill="none" stroke="#fff" stroke-width="1.2"/><circle cx="8" cy="10.8" r="0.6" fill="#fff"/></svg>
      +44 (0)7700 900 318
    </li>
    <li class="contacts__item">
      <svg class="icon" viewBox="0 0 16 16" aria-hidden="true"><circle cx="8" cy="8" r="8" fill="var(--brand-green)"/><rect x="4" y="5.2" width="8" height="5.6" fill="none" stroke="#fff" stroke-width="1.1"/><path d="M4 5.4 8 8.4l4-3" fill="none" stroke="#fff" stroke-width="1.1"/></svg>
      cprewett@vt-meridian.example.co.uk
    </li>
    <li class="contacts__item">
      <svg class="icon" viewBox="0 0 16 16" aria-hidden="true"><circle cx="8" cy="8" r="8" fill="var(--brand-green)"/><circle cx="8" cy="8" r="4.2" fill="none" stroke="#fff" stroke-width="1"/><ellipse cx="8" cy="8" rx="1.8" ry="4.2" fill="none" stroke="#fff" stroke-width="1"/><path d="M3.8 8h8.4" stroke="#fff" stroke-width="1"/></svg>
      www.vt-meridian.example.co.uk
    </li>
  </ul>
</section>

</body>
</html>
```